Investment Funding, Building and Construction

I need a design logo for my new business based out of Houston, TX called Kestrel Ridge Holdings LLC., We are a company looking to help fund and invest into other small/businesses that do not want to deal with the banking system. We also remodel, renovate, and build from the ground up anything from residential, industrial warehousing, and commercial buildings. We would like the design to express our great deal of passion that we have for the work, our dedication to helping the costumer/businesses receive their expectation of work and also our professionalism and commitment to making sure we get the job done as perfect as possible. We want to build your future!

Target Market(s)

Architects, Design Companies, Home Owners and Real Estate

Industry/Entity Type

Construction Company

Contact Information for Business Card

Name: Dorian Welsby
Position: CEO/President
Company Name: Kestrel Ridge Holdings LLC.,
Website: www.kestrelridgeholds.example
Phone: 281-555-0173
Email: kestrelridgeholds@mailbox.example, crewfundline@mailbox.example

Font styles to use
Serif

Colors
f04a50
3377b5

Requirements
Must have
• Motivational, Inspiring, and Detailed oriented work but simple.
Nice to have
• I would like to see excitement and enthusiasm within the card.
Should not have
• The project can not be boring and lack of detail.

```html
<!DOCTYPE html>
<html lang="en">
<head>
<meta charset="utf-8">
<title>Kestrel Ridge Holdings LLC. – Business Card</title>
<link rel="stylesheet" href="https://fonts.googleapis.com/css2?family=Arimo:wght@400;700&family=Open+Sans:wght@400;700&display=swap">
<style>
  :root {
    --card-white: #ffffff;
    --brand-blue: #3083f0;
    --accent-red: #ff2255;
    --accent-pink: #ff5192;
    --icon-teal: #66f2c4;
    --ink: #1a1a1a;
  }
  html, body {
    margin: 0;
    padding: 0;
    width: 1200px;
    height: 720px;
    overflow: hidden;
    background: var(--card-white);
  }
  .card {
    position: relative;
    width: 1200px;
    height: 720px;
    overflow: hidden;
    background: var(--card-white);
    font-family: "Arimo", Arial, sans-serif;
  }
  .card-shapes {
    position: absolute;
    inset: 0;
    width: 1200px;
    height: 720px;
  }
  .shape-red { fill: var(--accent-red); }
  .shape-pink { fill: var(--accent-pink); }
  .shape-white { fill: var(--card-white); }
  .shape-blue { fill: var(--brand-blue); }

  .holder-name {
    position: absolute;
    left: 103px;
    top: 140px;
    margin: 0;
    font-family: "Open Sans", Arial, sans-serif;
    font-size: 42px;
    font-weight: 400;
    color: var(--card-white);
    line-height: 1;
    letter-spacing: -0.5px;
  }
  .holder-name .surname { font-weight: 700; }
  .holder-title {
    position: absolute;
    left: 110px;
    top: 194px;
    margin: 0;
    font-size: 23px;
    font-weight: 700;
    letter-spacing: 0.5px;
    color: var(--card-white);
    line-height: 1;
  }

  .contact-list {
    position: absolute;
    left: 0;
    top: 0;
    margin: 0;
    padding: 0;
    list-style: none;
  }
  .contact-item {
    position: absolute;
    left: 108px;
    display: flex;
    align-items: center;
    gap: 22px;
    color: var(--card-white);
    font-size: 24px;
    line-height: 1.1;
    white-space: nowrap;
  }
  .contact-item.phone { top: 287px; }
  .contact-item.email { top: 398px; }
  .contact-item.web { top: 519px; }
  .contact-icon {
    width: 58px;
    height: 58px;
    flex: none;
  }
  .contact-icon circle { fill: none; stroke: var(--icon-teal); stroke-width: 4; }
  .contact-icon .glyph { fill: var(--icon-teal); }
  .contact-icon .glyph-line { stroke: var(--icon-teal); stroke-width: 3; fill: none; }

  .brand-block {
    position: absolute;
    left: 640px;
    width: 560px;
    text-align: center;
    color: var(--ink);
    margin: 0;
  }
  .logo-placeholder {
    top: 292px;
    font-size: 44px;
    letter-spacing: -2.5px;
    line-height: 1;
    font-weight: 400;
  }
  .company-name {
    top: 386px;
    font-size: 37px;
    letter-spacing: -1.5px;
    line-height: 1;
    font-weight: 400;
  }
</style>
</head>
<body>
  <main class="card">
    <svg class="card-shapes" viewBox="0 0 1131 675" preserveAspectRatio="none" aria-hidden="true">
      <path class="shape-red" d="M340,0 H1131 V675 H600 Z"/>
      <path class="shape-pink" d="M622,0 H1131 V675 H640 C560,480 545,210 622,0 Z"/>
      <path class="shape-white" d="M800,0 H1131 V675 H770 C700,600 640,540 625,470 C590,400 565,320 570,250 C578,120 680,25 800,0 Z"/>
      <path class="shape-blue" d="M0,0 H350 C455,60 540,200 588,345 C615,430 630,480 650,520 C690,590 730,635 770,675 H0 Z"/>
    </svg>

    <h1 class="holder-name">Dorian <span class="surname">WELSBY</span></h1>
    <p class="holder-title">CEO/PRESIDENT</p>

    <ul class="contact-list">
      <li class="contact-item phone">
        <svg class="contact-icon" viewBox="0 0 58 58" aria-hidden="true">
          <circle cx="29" cy="29" r="26"/>
          <path class="glyph" d="M22,20 c1.5,-1.5 3,-1 3.8,0.5 l1.8,3 c0.6,1.2 0.2,2.2 -0.8,2.9 l-1.2,0.9 c1,2.5 3,4.5 5.5,5.6 l0.9,-1.2 c0.7,-1 1.8,-1.4 2.9,-0.8 l3,1.8 c1.5,0.8 1.9,2.3 0.5,3.8 l-1.4,1.4 c-1.5,1.5 -4.5,1.4 -8.5,-1.2 c-3.5,-2.3 -6.5,-5.3 -8.3,-8.6 c-2,-3.6 -2,-6.2 -0.4,-7.7 Z"/>
        </svg>
        <span>+281-555-0173</span>
      </li>
      <li class="contact-item email">
        <svg class="contact-icon" viewBox="0 0 58 58" aria-hidden="true">
          <circle cx="29" cy="29" r="26"/>
          <path class="glyph" d="M38,20 L20,28 L27.5,30.5 L30,38 Z"/>
        </svg>
        <span>kestrelridgeholds@mailbox.example<br>crewfundline@mailbox.example</span>
      </li>
      <li class="contact-item web">
        <svg class="contact-icon" viewBox="0 0 58 58" aria-hidden="true">
          <circle cx="29" cy="29" r="26"/>
          <path class="glyph-line" d="M35,22 L23,29 L35,36"/>
          <circle class="glyph" cx="35" cy="22" r="4" style="stroke:none"/>
          <circle class="glyph" cx="23" cy="29" r="4" style="stroke:none"/>
          <circle class="glyph" cx="35" cy="36" r="4" style="stroke:none"/>
        </svg>
        <span>www.kestrelridgeholds.example</span>
      </li>
    </ul>

    <p class="brand-block logo-placeholder">LOGO HEAR</p>
    <p class="brand-block company-name">Kestrel Ridge Holdings LLC.</p>
  </main>
</body>
</html>
```